Dog care service needs advertising poster

Our company is Pawfield Haven. We provide care for dogs while their owners are away, either through home visits or a holiday stay in the homes of carefully selected minders. Our existing website & Facebook cover should provide all the colour cues for a poster - namely blues, blondes and grey. We have an existing logo (provided). We can feature the same imagery from our website as I have purchased the rights to the stock images.

www.pawfieldhaven.com.au
www.facebook.com/pawfieldhavenau

This brief is for design of a poster that can be placed in vet surgeries, groomers, on community noticeboards. It should be scalable to print in three sizes, A5, A4 & A3.

We wish to clearly communicate our three areas of service "dog minding, home visits, dog walking".

We would like to have the files ready for upload to Printlorra (or similar) for immediate printing.

Target Market(s)

Dog owners who love their dogs like family.

Industry/Entity Type

Advertising

Font styles to use
Sans Serif

Colors
33a6d7
3276b5

Requirements
Must have
• Logo
• www.pawfieldhaven.com.au
• Telephone number
• Three services - Dog Minding, Home Visits, Dog Walking
Nice to have
• use of our existing stock photography to highlight the three areas of service - Dog minding, home visits, dog walking. Existing colour palette - blues, blondes and grey.
• Text that can be used:
• Western Sydney’s complete dog care service.
• Dog Minding - Your dog stays in the home of one of our carefully selected minders.Treated like part of the family, they enjoy all the creature comforts they are used to.
• Home Visits - We visit your dog at your home for feeding, walking and playtime. Short of long visits available.
• Dog Walking - If you can't walk your dog for any reason we are here to help. 1/2 hour or hourly walks available.
• Contact us today for a tailored package to meet your needs.
Should not have
• Any additional illustrations beyond the logo.

```html
<!DOCTYPE html>
<html lang="en">
<head>
<meta charset="utf-8">
<title>Pawfield Haven – Dog Care Poster</title>
<link rel="stylesheet" href="https://fonts.googleapis.com/css2?family=Montserrat:wght@600;700;800&family=Open+Sans:wght@400;600&display=swap">
<style>
  :root {
    --sky-blue: #33a6d7;
    --deep-blue: #3276b5;
    --band-blue: #2c8ed0;
    --navy: #1f2f4a;
    --ink: #26344f;
    --paper: #ffffff;
    --backdrop: #e4e4e4;
    --body-text: #333a44;
  }
  * { box-sizing: border-box; margin: 0; padding: 0; }
  html, body {
    width: 1200px; height: 789px; overflow: hidden;
    background: var(--backdrop);
  }
  .poster {
    position: absolute; left: 335px; top: 20px;
    width: 530px; height: 750px;
    background: var(--paper);
    overflow: hidden;
    box-shadow: 0 6px 18px rgba(0,0,0,.18);
    font-family: "Open Sans", Arial, sans-serif;
  }
  .header-band {
    position: absolute; inset: 0 0 auto 0; height: 130px;
    background: linear-gradient(115deg, var(--deep-blue) 0%, var(--sky-blue) 60%, var(--deep-blue) 100%);
  }
  .header-band::after {
    content: ""; position: absolute; right: 0; top: 0;
    width: 140px; height: 130px;
    background: linear-gradient(160deg, #2a3b57, #17233a);
    clip-path: polygon(45% 0, 100% 0, 100% 100%, 0 100%);
    opacity: .85;
  }
  .logo-plate {
    position: absolute; left: 170px; top: 16px; z-index: 3;
    width: 190px; height: 64px;
    background: var(--paper);
    border-radius: 12px;
    box-shadow: 0 2px 6px rgba(0,0,0,.25);
    display: flex; align-items: center; justify-content: center; gap: 10px;
  }
  .logo-dot { width: 18px; height: 18px; border-radius: 50%; background: var(--deep-blue); }
  .logo-name {
    font-family: "Montserrat", Arial, sans-serif; font-weight: 700;
    font-size: 19px; color: var(--ink);
  }
  .hero-photo {
    position: absolute; left: 0; right: 0; top: 100px; height: 490px;
    background:
      radial-gradient(ellipse 48% 45% at 78% 48%, #c99a4e 0%, #b07d36 55%, transparent 75%),
      linear-gradient(180deg, #8fc2e4 0%, #bcd9ea 22%, #9eb0b4 34%, #a9a294 55%, #8e8a80 100%);
  }
  .headline-strip {
    position: absolute; left: 0; right: 0; top: 108px; z-index: 2;
    height: 80px;
    background: rgba(235,238,242,.9);
    text-align: center;
    font-family: "Montserrat", Arial, sans-serif; font-weight: 800;
    padding-top: 12px; line-height: 1.15;
  }
  .headline-strip .lead { font-size: 23px; color: var(--ink); letter-spacing: .3px; }
  .headline-strip .accent { font-size: 23px; color: var(--sky-blue); }
  .service-card {
    position: absolute; z-index: 2;
    width: 165px; height: 190px;
    background: var(--paper);
    padding: 7px;
    box-shadow: 0 3px 8px rgba(0,0,0,.3);
    text-align: center;
  }
  .service-card .card-photo { height: 98px; }
  .service-card h3 {
    font-family: "Montserrat", Arial, sans-serif; font-weight: 700;
    font-size: 15px; color: var(--band-blue); margin: 6px 0 3px;
  }
  .service-card p { font-size: 8.4px; line-height: 1.3; color: var(--body-text); }
  .card-minding { left: 22px; top: 345px; transform: rotate(-4deg); }
  .card-visits { left: 182px; top: 365px; transform: rotate(-5deg); }
  .card-walking { left: 345px; top: 350px; transform: rotate(2deg); }
  .card-minding .card-photo { background: linear-gradient(180deg, #8fc7e8 0%, #6a6a5a 45%, #6fa33c 100%); }
  .card-visits .card-photo { background: linear-gradient(180deg, #ece9e3 0%, #d8c8b0 40%, #9a7245 100%); }
  .card-walking .card-photo { background: linear-gradient(180deg, #c9d9c8 0%, #d9c6a8 45%, #6b9a3a 100%); }
  .contact-band {
    position: absolute; left: 0; right: 0; top: 585px; height: 130px;
    background: linear-gradient(180deg, var(--sky-blue), var(--band-blue));
    color: var(--paper);
  }
  .contact-call {
    position: absolute; left: 40px; top: 28px;
    font-family: "Montserrat", Arial, sans-serif; font-weight: 600;
    font-size: 14.5px; line-height: 1.3;
  }
  .contact-lines {
    position: absolute; left: 260px; top: 40px;
    font-family: "Montserrat", Arial, sans-serif; font-weight: 600;
  }
  .contact-line { display: flex; align-items: center; gap: 12px; margin-bottom: 12px; }
  .contact-line svg { width: 18px; height: 18px; fill: var(--paper); }
  .phone-number { font-size: 16px; letter-spacing: .5px; }
  .web-address { font-size: 13px; }
  .base-strip {
    position: absolute; left: 0; right: 0; bottom: 0; height: 35px;
    background: var(--navy);
  }
</style>
</head>
<body>
  <main class="poster">
    <div class="header-band"></div>
    <div class="hero-photo" role="img" aria-label="Golden retriever puppy looking out of a car window at a sandy beach under a blue sky"></div>

    <div class="logo-plate">
      <span class="logo-dot"></span>
      <span class="logo-name">Pawfield Haven</span>
    </div>

    <header class="headline-strip">
      <div class="lead">WESTERN SYDNEY’S COMPLETE</div>
      <div class="accent">DOG CARE SERVICE</div>
    </header>

    <article class="service-card card-minding">
      <div class="card-photo" role="img" aria-label="Australian shepherd dog sitting on green grass"></div>
      <h3>Dog Minding</h3>
      <p>Your dog stays in the home of one of our carefully selected minders. Treated like part of the family, they enjoy all the creature comforts they are used to.</p>
    </article>

    <article class="service-card card-visits">
      <div class="card-photo" role="img" aria-label="Small terrier sitting on a home doormat"></div>
      <h3>Home Visits</h3>
      <p>We visit your dog at your home for feeding, walking and playtime. Short or long visits available.</p>
    </article>

    <article class="service-card card-walking">
      <div class="card-photo" role="img" aria-label="Bulldog on a lead standing on a lawn"></div>
      <h3>Dog Walking</h3>
      <p>If you can't walk your dog for any reason we are here to help. 1/2 hour or hourly walks available.</p>
    </article>

    <section class="contact-band">
      <p class="contact-call">Contact us today<br>for a tailored package<br>to meet your needs.</p>
      <div class="contact-lines">
        <div class="contact-line">
          <svg viewBox="0 0 24 24" aria-hidden="true"><path d="M6.6 10.8a15.1 15.1 0 0 0 6.6 6.6l2.2-2.2a1 1 0 0 1 1-.25 11.4 11.4 0 0 0 3.6.57 1 1 0 0 1 1 1V20a1 1 0 0 1-1 1A17 17 0 0 1 3 4a1 1 0 0 1 1-1h3.5a1 1 0 0 1 1 1c0 1.25.2 2.45.57 3.57a1 1 0 0 1-.25 1z"/></svg>
          <span class="phone-number">0400 555 318</span>
        </div>
        <div class="contact-line">
          <svg viewBox="0 0 24 24" aria-hidden="true"><path d="M2 4h20v12H2zM4 6v8h16V6zM9 18h6v2H9z"/></svg>
          <span class="web-address">www.pawfieldhaven.com.au</span>
        </div>
      </div>
    </section>
    <div class="base-strip"></div>
  </main>
</body>
</html>
```